Coffee bag stamp design for new coffee brand

Stamp design that will be used like a label on a coffee package.
It must be a vector that can be produced as a stamp. Coffee bag is from brown craft paper. I upload image of this bag. Size of design is 80mm x 140mm.
I also uploaded two pictures for inspiration, but I will also appreciate new ideas.

Target Market(s)

Coffee lovers, who love to try new coffee. Also hipsters.

Colors

Designer to choose only greyscale colors for use in the design.

Requirements
Must have
• Some information about coffee must have:
Name: BRAZIL (the biggest font in that design)
Region: Santos
Altitude: 60 – 1200 m.n.m.
Variety: Arabica
Processing: unwashed

```html
<!DOCTYPE html>
<html lang="en">
<head>
<meta charset="utf-8">
<title>Alder House – Brazil Santos Stamp</title>
<link rel="stylesheet" href="https://fonts.googleapis.com/css2?family=Passion+One&family=Oswald:wght@500&family=Roboto:wght@400&family=Tinos:wght@400;700&display=swap">
<style>
  :root {
    --kraft: #c9a47c;
    --ink: #161514;
    --bean: #6f5a44;
  }
  * { margin: 0; padding: 0; box-sizing: border-box; }
  html, body { width: 757px; height: 1200px; overflow: hidden; background: var(--kraft); }
  .canvas { position: relative; width: 757px; height: 1200px; color: var(--ink); }
  .frame { position: absolute; left: 0; top: 0; }
  .line { position: absolute; left: 0; width: 757px; text-align: center; white-space: nowrap; }
  .variety { top: 24px; font: 56px/1 "Passion One", sans-serif; letter-spacing: 1px; }
  .brand-name { top: 322px; font: 400 38px/1 "Roboto", sans-serif; letter-spacing: 1px; }
  .bar { position: absolute; left: 234px; width: 288px; display: flex; align-items: center; justify-content: center; }
  .bar-origin { top: 520px; height: 56px; font: 500 50px/1 "Oswald", sans-serif; letter-spacing: 1px; }
  .bar-origin::before, .bar-origin::after { content: ""; position: absolute; top: 0; width: 28px; height: 100%; background: var(--ink); }
  .bar-origin::before { left: 0; }
  .bar-origin::after { right: 0; }
  .bar-label { background: var(--ink); color: var(--kraft); font: 400 30px/1 "Roboto", sans-serif; }
  .bar-altitude { top: 677px; height: 52px; }
  .bar-processing { top: 814px; height: 48px; }
  .region { top: 606px; font: 400 30px/1 "Roboto", sans-serif; }
  .value { font: 400 29px/1 "Tinos", serif; }
  .altitude-value { top: 756px; }
  .processing-value { top: 888px; }
  .weight { top: 972px; font: 700 31px/1 "Tinos", serif; letter-spacing: 1px; }
  .bean { position: absolute; background: var(--bean); border-radius: 50%; opacity: .55; }
</style>
</head>
<body>
<main class="canvas">
  <svg class="frame" width="757" height="1200" viewBox="0 0 757 1200" aria-hidden="true">
    <path d="M234 876 V304 A144 144 0 0 1 522 304 V876 A144 144 0 0 1 234 876 Z" fill="none" stroke="var(--ink)" stroke-width="4"/>
    <line x1="264" y1="440" x2="492" y2="440" stroke="var(--ink)" stroke-width="2"/>
  </svg>

  <p class="line variety">ARABICA</p>
  <p class="line brand-name">ALDER HOUSE</p>

  <div class="bar bar-origin">BRAZIL</div>
  <p class="line region">SANTOS</p>

  <div class="bar bar-label bar-altitude">ALTITUDE:</div>
  <p class="line value altitude-value">60 – 1200 m.n.m.</p>

  <div class="bar bar-label bar-processing">PROCESSING:</div>
  <p class="line value processing-value">unwashed</p>

  <p class="line weight">100 g</p>

  <div class="bean" role="img" aria-label="Sketched coffee beans" style="left:156px;top:507px;width:37px;height:77px;"></div>
  <div class="bean" role="img" aria-label="Sketched coffee bean" style="left:540px;top:406px;width:37px;height:40px;"></div>
  <div class="bean" role="img" aria-label="Sketched coffee bean" style="left:559px;top:737px;width:69px;height:70px;"></div>
  <div class="bean" role="img" aria-label="Sketched coffee bean" style="left:134px;top:844px;width:81px;height:83px;"></div>
  <div class="bean" role="img" aria-label="Sketched cluster of coffee beans" style="left:378px;top:1025px;width:148px;height:119px;"></div>
</main>
</body>
</html>
```